Business Card for Wellness Clinic

We need a business card for our new logo. I want it to match the feel of the logo

Target Market(s)

Young professional families looking for holistic health care

Industry/Entity Type

Health And Wellness

Contact Information for Business Card

Our business Name: Larkvale Health & wellness Centre, our phone #, email address...see attached old business card

Font styles to use
Sans Serif

Colors
33b8a4
cee9f5

Requirements
Must have
• my logo and business name
• Font is "Helvetica Neue LT Std 45 Light" and
• Only for "&" using font "Trajan pro bold"
• Use colors in the logo

```html
<!DOCTYPE html>
<html lang="en">
<head>
<meta charset="utf-8">
<title>Larkvale Health &amp; Wellness Centre — Business Card</title>
<link rel="stylesheet" href="https://fonts.googleapis.com/css2?family=Roboto:wght@300;400;700&display=swap">
<style>
  :root {
    --teal: #33b8a4;
    --teal-deep: #22a891;
    --teal-light: #4cc6b2;
    --mist: #cee9f5;
    --white: #ffffff;
    --paper: #f6f7f7;
    --paper-shade: #e4e6e6;
    --ink: #3c3f41;
    --rule: #9ea3a4;
    --backdrop: #dcdfe0;
  }
  * { box-sizing: border-box; margin: 0; padding: 0; }
  html, body { width: 1200px; height: 950px; overflow: hidden; }
  body {
    background: var(--backdrop);
    font-family: "Roboto", "Helvetica Neue", Arial, sans-serif;
    font-weight: 300;
    display: flex;
    flex-direction: column;
    align-items: center;
    justify-content: center;
    gap: 50px;
  }
  .card {
    position: relative;
    width: 700px;
    height: 400px;
    overflow: hidden;
    box-shadow: 0 6px 18px rgba(0,0,0,0.18);
  }

  /* Appointment side */
  .card--appointment {
    background: linear-gradient(135deg, var(--white) 0%, var(--paper) 55%, var(--paper-shade) 100%);
  }
  .brand--teal {
    position: absolute;
    left: 150px;
    top: 58px;
    color: var(--teal);
  }
  .brand__name {
    font-size: 27px;
    letter-spacing: 6px;
    text-transform: uppercase;
    font-weight: 300;
    line-height: 1.1;
  }
  .brand__sub {
    font-size: 14px;
    letter-spacing: 7px;
    text-transform: uppercase;
    font-weight: 300;
    margin-top: 4px;
    padding-left: 4px;
  }
  .field {
    position: absolute;
    display: flex;
    align-items: flex-end;
    color: var(--teal);
    font-size: 18px;
    font-weight: 400;
  }
  .field__line {
    flex: 1;
    border-bottom: 1.5px solid var(--rule);
    margin-left: 10px;
    height: 1px;
  }
  .field--time { left: 360px; right: 40px; top: 170px; }
  .field--date { left: 40px; right: 40px; top: 248px; }
  .notice {
    position: absolute;
    left: 40px;
    right: 40px;
    top: 300px;
    color: var(--ink);
    font-size: 17px;
    font-weight: 400;
    line-height: 1.35;
    text-align: center;
  }

  /* Contact side */
  .card--contact {
    background: linear-gradient(125deg, var(--teal-light) 0%, var(--teal) 45%, var(--teal-deep) 100%);
    color: var(--white);
  }
  .brand--white {
    position: absolute;
    left: 70px;
    top: 48px;
    color: var(--white);
  }
  .brand--white .brand__name { font-size: 25px; letter-spacing: 5px; }
  .brand--white .brand__sub { font-size: 13px; letter-spacing: 7px; }
  .person {
    position: absolute;
    left: 48px;
    top: 150px;
  }
  .person__name {
    font-size: 25px;
    font-weight: 700;
    letter-spacing: 0.3px;
  }
  .person__role {
    font-size: 19px;
    font-weight: 300;
    margin-top: 2px;
  }
  .address {
    font-style: normal;
    font-size: 18px;
    line-height: 1.35;
    margin-top: 14px;
  }
  .contact-list {
    list-style: none;
    margin-top: 6px;
    font-size: 18px;
    line-height: 1.4;
  }
  .contact-list li { display: flex; align-items: center; gap: 8px; }
  .contact-list svg { width: 17px; height: 17px; flex: none; }
  .motif-area {
    position: absolute;
    right: 0;
    bottom: 0;
    width: 310px;
    height: 270px;
    border-top-left-radius: 100% 100%;
    background: radial-gradient(circle at 70% 70%, rgba(255,255,255,0.95) 0%, rgba(255,255,255,0.75) 55%, rgba(255,255,255,0.35) 100%);
  }
</style>
</head>
<body>

  <section class="card card--appointment" aria-label="Appointment card">
    <div class="brand brand--teal">
      <div class="brand__name">Larkvale Health</div>
      <div class="brand__sub">&amp; Wellness Centre</div>
    </div>
    <div class="field field--time"><span>Time :</span><span class="field__line"></span></div>
    <div class="field field--date"><span>Date :</span><span class="field__line"></span></div>
    <p class="notice">If you are unable to keep your appointment, please provide<br>2 business days notice or full visit fees will apply</p>
  </section>

  <section class="card card--contact" aria-label="Contact card">
    <div class="brand brand--white">
      <div class="brand__name">Larkvale Health</div>
      <div class="brand__sub">&amp; Wellness Centre</div>
    </div>
    <div class="person">
      <h1 class="person__name">Dr. Maren Holt, N.D.</h1>
      <p class="person__role">Naturopathic Doctor</p>
      <address class="address">48 Alder Row, Suite 120<br>Brookhaven, ON K4R 2M7</address>
      <ul class="contact-list">
        <li>
          <svg viewBox="0 0 24 24" aria-hidden="true"><path fill="#fff" d="M6.6 10.8a15.1 15.1 0 0 0 6.6 6.6l2.2-2.2a1 1 0 0 1 1-.25 11.4 11.4 0 0 0 3.6.57 1 1 0 0 1 1 1V20a1 1 0 0 1-1 1A17 17 0 0 1 3 4a1 1 0 0 1 1-1h3.5a1 1 0 0 1 1 1c0 1.25.2 2.45.57 3.57a1 1 0 0 1-.25 1z"/></svg>
          <span>555-014-3827</span>
        </li>
        <li>
          <svg viewBox="0 0 24 24" aria-hidden="true"><rect x="2" y="5" width="20" height="14" rx="1.5" fill="#fff"/><path d="M3 6.5l9 6.5 9-6.5" fill="none" stroke="#33b8a4" stroke-width="1.6"/></svg>
          <span>mholt@larkvalewellness.ca</span>
        </li>
        <li>
          <svg viewBox="0 0 24 24" aria-hidden="true"><circle cx="12" cy="12" r="10" fill="#fff"/><path d="M2 12h20M12 2c3 3 3 17 0 20M12 2c-3 3-3 17 0 20" fill="none" stroke="#33b8a4" stroke-width="1.4"/></svg>
          <span>www.larkvalewellness.ca</span>
        </li>
      </ul>
    </div>
    <div class="motif-area" role="img" aria-label="Large white leaf motif from the clinic mark"></div>
  </section>

</body>
</html>
```